LOGO DESIGN: Construction Related Service Business

We require a logo for our business Tovar Services. We are a construction related business offering a range of services including machine services for groundworks (digging trenches, soak wells, preparing land for construction etc), demolition and truck haulage from demolition sites.
We would like our logo to be predominately text, but may include abstract graphics. The colour scheme should be mainly a mid bright blue and overall be quite 'clean'.

Industry/Entity Type

Construction

Contact Information for Business Card

Dale Morrow
Ph:041 592 3068
tovarservices@quillnet.com.au

Colors
0456a3

```html
<!DOCTYPE html>
<html lang="en">
<head>
<meta charset="utf-8">
<title>Tovar Services – Business Card</title>
<link rel="stylesheet" href="https://fonts.googleapis.com/css2?family=Source+Sans+3:wght@400;600;700&display=swap">
<style>
  :root {
    --card-bg: #e2e2cf;
    --band-blue: #1196d2;
    --brand-navy: #2e2f7f;
    --brand-blue: #1196d2;
    --ink: #3a3a3a;
  }
  * { margin: 0; padding: 0; box-sizing: border-box; }
  html, body {
    width: 1200px;
    height: 769px;
    overflow: hidden;
    background: var(--card-bg);
  }
  .card {
    position: relative;
    width: 1200px;
    height: 769px;
    background: var(--card-bg);
    font-family: "Source Sans 3", "Myriad Pro", Arial, sans-serif;
    color: var(--ink);
  }
  .side-band {
    position: absolute;
    left: 0;
    top: 0;
    width: 289px;
    height: 100%;
    background: var(--band-blue);
  }
  .holder-name {
    position: absolute;
    right: 112px;
    top: 68px;
    font-size: 52px;
    line-height: 1;
    letter-spacing: -0.5px;
    color: var(--ink);
    font-weight: 400;
  }
  .holder-name .first { font-weight: 700; }
  .brand {
    position: absolute;
    left: 396px;
    top: 364px;
    display: flex;
    align-items: center;
    gap: 22px;
  }
  .brand-dot {
    width: 58px;
    height: 58px;
    border-radius: 50%;
    background: var(--brand-blue);
    flex: none;
  }
  .brand-name {
    font-size: 60px;
    font-weight: 600;
    line-height: 1;
    letter-spacing: 1.5px;
    text-transform: uppercase;
    color: var(--brand-navy);
  }
  .contact {
    position: absolute;
    left: 289px;
    right: 0;
    top: 598px;
    text-align: center;
    font-size: 30px;
    line-height: 40px;
    color: var(--ink);
    padding-right: 40px;
  }
</style>
</head>
<body>
  <div class="card">
    <div class="side-band"></div>
    <p class="holder-name"><span class="first">Dale</span> Morrow</p>
    <div class="brand">
      <span class="brand-dot"></span>
      <span class="brand-name">Tovar Services</span>
    </div>
    <div class="contact">
      <p class="contact-phone">Phone : + 041 592 3068</p>
      <p class="contact-email">tovarservices@quillnet.com.au</p>
    </div>
  </div>
</body>
</html>
```